Business Card and Logo Color Scheme Design Contest

We are starting a new company called Lone Ridge Structural Partners and already have a logo however, the colors for the logo itself are not final and COULD be changed. I'm hoping to move AWAYfrom the gold color in the card and the logo as it seems a bit outdated. What we need help with is to find what our business color scheme will be, and then incorporate those colors into both the logo and the business card design itself. We also want to make sure we are known as "LRS" so in the future we can just refer to ourselves as "LRS" and not Lone Ridge Structural Partners. That being said, I would like to make a slight change to the logo to somehow include the letters "LRS." The logo used in the front of the card design MUST ALSO include the words "Firm No. 64307" within the logo. My vision is for the front of the card to have the information shown in the attached image. For the back of the card, I'm hoping to have something very simple. I'm envisioning a solid color with either the website (www.bridgemarkplans.com) and a simplified version of the logo. I've attached an example but I'm looking for a complete redesign. I'm looking for a slick, modern and simple design.

Industry/Entity Type

Civil Engineer

Contact Information for Business Card

Logo
Firm No. 64307
Marcus Holloway, PE
Chief Operating Officer
Email:mholloway@bridgemarkplans.com
Ph: 936.555.0142 | D: 936.555.0178 | M:210.555.0263
4187 W. Kellingham, Conroe, Texas 77301
www.bridgemarkplans.com

Requirements
Must have
• Logo
Contact Info
Nice to have
• "LRS" Incorporated in the design
Should not have
• The current color scheme

```html
<!DOCTYPE html>
<html lang="en">
<head>
<meta charset="utf-8">
<title>Lone Ridge Structural Partners — Business Card</title>
<link rel="stylesheet" href="https://fonts.googleapis.com/css2?family=Lato:ital,wght@0,400;0,700;0,900;1,400&display=swap">
<style>
  :root {
    --navy: #173a55;
    --green: #86e01e;
    --white: #ffffff;
    --backdrop: #cdd8c1;
    --ink-soft: #e9eef2;
  }
  * { box-sizing: border-box; margin: 0; padding: 0; }
  html, body {
    width: 988px; height: 1200px; overflow: hidden;
    background: var(--backdrop);
    font-family: "Lato", Arial, sans-serif;
  }
  .canvas { position: relative; width: 988px; height: 1200px; }

  .card { position: absolute; left: 124px; width: 741px; overflow: hidden; }

  /* Front */
  .card-front { top: 101px; height: 424px; display: flex; }
  .front-brand {
    width: 379px; height: 100%; background: var(--white);
    display: flex; align-items: center; justify-content: center;
  }
  .front-info {
    position: relative; flex: 1; height: 100%; background: var(--navy); color: var(--white);
  }

  .wordmark {
    display: flex; align-items: flex-start; gap: 14px;
    font-weight: 900; text-transform: uppercase; letter-spacing: 2px;
  }
  .wordmark-square { width: 22px; height: 22px; background: var(--green); flex: none; margin-top: 12px; }
  .wordmark-text { display: flex; flex-direction: column; }
  .wordmark-initials { font-size: 46px; line-height: 1; letter-spacing: 6px; margin-bottom: 8px; }
  .wordmark-name { font-size: 26px; line-height: 1.12; }
  .wordmark-firm { margin-top: 10px; font-size: 15px; letter-spacing: 3px; line-height: 1; }
  .front-brand .wordmark { color: var(--navy); }

  .person { position: absolute; left: 28px; top: 50px; }
  .person-name { font-size: 30px; font-weight: 700; letter-spacing: 0.2px; }
  .person-title { margin-top: 12px; font-size: 22px; font-style: italic; font-weight: 400; color: var(--ink-soft); }

  .contact-rail {
    position: absolute; left: 0; top: 241px; width: 57px; height: 158px;
    background: var(--green);
  }
  .contact-rail svg { position: absolute; left: 18px; width: 20px; height: 20px; fill: var(--white); }
  .icon-phone { top: 17px; }
  .icon-mail { top: 78px; }
  .icon-pin { top: 113px; }

  .contact-list { position: absolute; left: 74px; top: 0; list-style: none; font-size: 14.5px; line-height: 22px; white-space: nowrap; }
  .contact-list li { position: absolute; left: 0; }
  .contact-list .row-phone { top: 257px; }
  .contact-list .row-mobile { top: 281px; }
  .contact-list .row-mail { top: 318px; }
  .contact-list .row-address { top: 353px; }
  .contact-list .label { font-style: italic; }

  /* Back */
  .card-back { top: 663px; height: 407px; background: var(--white); }
  .back-field {
    height: 331px; background: var(--navy);
    display: flex; align-items: center; justify-content: center;
  }
  .back-field .wordmark { color: var(--white); }
  .back-field .wordmark-initials { font-size: 52px; }
  .back-field .wordmark-name { font-size: 28px; }
  .back-stripe { height: 10px; background: var(--green); }
  .back-web {
    height: 66px; display: flex; align-items: center; justify-content: center;
    font-size: 21px; letter-spacing: 3px; color: var(--navy); font-style: italic;
  }
</style>
</head>
<body>
<main class="canvas">

  <section class="card card-front" aria-label="Card front">
    <div class="front-brand">
      <div class="wordmark">
        <span class="wordmark-square" aria-hidden="true"></span>
        <span class="wordmark-text">
          <span class="wordmark-initials">LRS</span>
          <span class="wordmark-name">Lone Ridge<br>Structural<br>Partners</span>
          <span class="wordmark-firm">Firm No. 64307</span>
        </span>
      </div>
    </div>
    <div class="front-info">
      <div class="person">
        <h1 class="person-name">Marcus Holloway, PE</h1>
        <p class="person-title">Chief Operating Officer</p>
      </div>
      <div class="contact-rail" aria-hidden="true">
        <svg class="icon-phone" viewBox="0 0 24 24"><path d="M6.6 10.8a15.1 15.1 0 0 0 6.6 6.6l2.2-2.2a1 1 0 0 1 1-.25 11.4 11.4 0 0 0 3.6.57 1 1 0 0 1 1 1V20a1 1 0 0 1-1 1A17 17 0 0 1 3 4a1 1 0 0 1 1-1h3.5a1 1 0 0 1 1 1c0 1.25.2 2.45.57 3.57a1 1 0 0 1-.25 1z"/></svg>
        <svg class="icon-mail" viewBox="0 0 24 24"><path d="M2 5h20v14H2z M3.5 6.5v.4L12 12.5l8.5-5.6v-.4z" fill-rule="evenodd"/></svg>
        <svg class="icon-pin" viewBox="0 0 24 24"><path d="M12 2a7 7 0 0 0-7 7c0 5.2 7 13 7 13s7-7.8 7-13a7 7 0 0 0-7-7zm0 9.5A2.5 2.5 0 1 1 12 6.5a2.5 2.5 0 0 1 0 5z"/></svg>
      </div>
      <ul class="contact-list">
        <li class="row-phone">936.555.0142 &nbsp;- (<span class="label">direct</span>) 936.555.0178</li>
        <li class="row-mobile">(<span class="label">mobile</span>) 210.555.0263</li>
        <li class="row-mail">mholloway@bridgemarkplans.com</li>
        <li class="row-address">4187 W. Kellingham, Conroe, Texas 77301</li>
      </ul>
    </div>
  </section>

  <section class="card card-back" aria-label="Card back">
    <div class="back-field">
      <div class="wordmark">
        <span class="wordmark-square" aria-hidden="true"></span>
        <span class="wordmark-text">
          <span class="wordmark-initials">LRS</span>
          <span class="wordmark-name">Lone Ridge<br>Structural<br>Partners</span>
        </span>
      </div>
    </div>
    <div class="back-stripe"></div>
    <p class="back-web">www.bridgemarkplans.com</p>
  </section>

</main>
</body>
</html>
```